Advertisement Design Project

Attached is the information I need in a big color ad

10X11 that will go in a weekly local paper.
I am open to color and graphics-no pictures of people please.

My logo is also attached, which I would like in the ad.

Sorry for the short notice-I just got a deal on the space and it is due Friday.

```html
<!DOCTYPE html>
<html lang="en">
<head>
<meta charset="utf-8">
<title>New Tax Laws Workshop Ad</title>
<link rel="stylesheet" href="https://fonts.googleapis.com/css2?family=Open+Sans:wght@400;700;800&display=swap">
<style>
  :root {
    --clay: #d29b7b;
    --gold: #fcc457;
    --amber: #fbb934;
    --cream: #fee0a8;
    --white: #ffffff;
    --tagline: #f7b531;
  }
  html, body { margin: 0; padding: 0; overflow: hidden; }
  body { width: 1200px; height: 1000px; background: var(--white); position: relative; font-family: "Open Sans", Arial, sans-serif; }
  .ad { position: absolute; left: 230px; top: 103px; width: 772px; height: 827px; overflow: hidden; background: var(--clay); }
  .ad-shapes { position: absolute; left: 0; top: 0; }
  .brand { position: absolute; left: 40px; top: 150px; width: 210px; text-align: center; color: var(--cream); font-weight: 800; font-size: 30px; line-height: 1.1; }
  .brand-dot { display: block; width: 44px; height: 44px; border-radius: 50%; background: var(--amber); margin: 0 auto 14px; }
  .headline { position: absolute; left: 235px; top: 152px; margin: 0; color: var(--white); font-weight: 700; font-size: 46px; line-height: 44px; }
  .subhead { position: absolute; left: 237px; top: 259px; margin: 0; color: var(--white); font-weight: 700; font-size: 27px; }
  .details { position: absolute; left: 0; top: 352px; width: 297px; height: 475px; background: var(--amber); color: var(--white); font-size: 15px; }
  .details p { margin: 0; position: absolute; left: 30px; right: 10px; line-height: 23px; }
  .details strong { font-weight: 700; }
  .presenter { top: 30px; }
  .values { top: 153px; font-weight: 700; }
  .values .sep { display: inline-block; width: 8px; height: 8px; border-radius: 50%; background: var(--white); margin: 0 12px; vertical-align: 8px; }
  .times-label { top: 183px; left: 0 !important; right: 0 !important; text-align: center; line-height: 18px !important; }
  .times { top: 243px; }
  .venue { top: 287px; font-weight: 700; }
  .reserve { top: 382px; line-height: 17px !important; }
  .topics { position: absolute; left: 325px; top: 351px; margin: 0; padding: 0; list-style: none; color: var(--white); font-weight: 700; font-size: 14.5px; }
  .topics li { position: relative; padding-left: 11px; height: 29.3px; line-height: 20px; }
  .topics li::before { content: ""; position: absolute; left: 0; top: 6px; width: 8px; height: 8px; border-radius: 50%; background: var(--amber); }
  .topics li.cont::before { display: none; }
  .tagline { position: absolute; left: 318px; top: 738px; margin: 0; color: var(--tagline); font-weight: 700; font-size: 19px; line-height: 29px; text-shadow: 1px 1px 1px rgba(150, 90, 40, 0.5); }
</style>
</head>
<body>
<div class="ad">
  <svg class="ad-shapes" width="772" height="827" viewBox="0 0 772 827" aria-hidden="true">
    <path d="M475 0 C640 150 760 380 772 827 L772 0 Z" fill="var(--gold)"/>
    <path d="M660 0 C720 170 765 430 772 827 L772 0 Z" fill="var(--cream)"/>
    <polygon points="0,327 310,357 297,352 0,352" fill="var(--cream)"/>
  </svg>

  <div class="brand"><span class="brand-dot"></span>Marsh Law</div>

  <h1 class="headline">New Tax Laws<br>Trusts</h1>
  <h2 class="subhead">Annuities abd long Term Care</h2>

  <section class="details">
    <p class="presenter"><strong>Presented by:</strong> dana whitfield marsh<br>Attorney at Law<br>2140 Harbor Lane, Soquel.<br>Helping Families plan their estates<br>for&nbsp; over&nbsp; 20 years.</p>
    <p class="values">Tust<span class="sep"></span>Relationship<span class="sep"></span>Integrity</p>
    <p class="times-label">Workshop Times:<br>September 19,2013</p>
    <p class="times">&nbsp;1-2:30 pm &nbsp;&nbsp;&nbsp;- &nbsp;&nbsp;&nbsp;&nbsp;6 - 7:30 pm</p>
    <p class="venue">Bayview Garden Inn, aptos<br>&nbsp;&nbsp;4820 Coastline Drive<br>&nbsp;&nbsp;&nbsp;Aptos, California 95003</p>
    <p class="reserve"><strong>Seating is limited for a Reservation<br>please call</strong><br>(831) 555-0142</p>
  </section>

  <ul class="topics">
    <li>Come learn what you need to now</li>
    <li>Is a living trust right forme?</li>
    <li>Does my existing Trust need to be changed?</li>
    <li>Why dose Joint Tenancy creat tax problems?</li>
    <li>I have a will, isn't that enough?</li>
    <li>Why do I need powers of attorney</li>
    <li>How much are inheritance taxes?</li>
    <li>What are the new Affordable Care Act taxes?</li>
    <li>How dose Long Term Care insurance work?</li>
    <li>The average cost of long term care is over 80K a year</li>
    <li class="cont">how do i plan those costs?</li>
    <li>The truth about annuites</li>
    <li>What are the biggest mistakes in estate planning?</li>
  </ul>

  <p class="tagline">Security = Good information + Good Planning<br>Be&nbsp; Smart. Plan Ahead</p>
</div>
</body>
</html>
```